Consulting company needs Business Cards - rough concept provided

I'm looking for someone to take our business card idea and make is slick and polished - to communicate our high-end, sophisticated, serious consulting business. We have a rough layout we did in-house. We are open to ideas on repo-ing elements, adjusting sizes, typefaces etc... within the general concept we've already come up with. We want it to be super-clean and sophisticated. We want to keep the white backgrounds, and blue brand colors. Our goal is to print with painted blue edges on thick cardstock. Thank you!!

```html
<!DOCTYPE html>
<html lang="en">
<head>
<meta charset="utf-8">
<title>Northvale Business Card</title>
<link href="https://fonts.googleapis.com/css2?family=Montserrat:wght@400;700;800;900&family=EB+Garamond:wght@400&display=swap" rel="stylesheet">
<style>
  :root {
    --backdrop: #3f3a36;
    --card: #262626;
    --ink: #ffffff;
    --brand-blue: #009ad8;
    --muted: #b8b8b8;
  }
  html, body {
    margin: 0;
    padding: 0;
    width: 1200px;
    height: 1200px;
    overflow: hidden;
    background: var(--backdrop);
  }
  .canvas {
    position: relative;
    width: 1200px;
    height: 1200px;
    font-family: "Montserrat", sans-serif;
    color: var(--ink);
  }
  .card {
    position: absolute;
    left: 179px;
    width: 861px;
    background: var(--card);
    box-shadow: 0 6px 18px rgba(0,0,0,0.35);
  }
  .card--back { top: 85px; height: 494px; }
  .card--front { top: 621px; height: 497px; }

  .mission {
    position: absolute;
    left: 0; right: 0;
    top: 94px;
    margin: 0;
    text-align: center;
    font-size: 37px;
    font-weight: 400;
    line-height: 78px;
    letter-spacing: 1.2px;
  }
  .mission .keyword { color: var(--brand-blue); font-weight: 700; }

  .wordmark {
    position: absolute;
    left: 0; right: 0;
    top: 2px;
    margin: 0;
    text-align: center;
    font-size: 104px;
    font-weight: 900;
    line-height: 1.1;
    letter-spacing: 2px;
    color: var(--ink);
  }
  .contact-name {
    position: absolute;
    left: 0; right: 0;
    top: 140px;
    margin: 0;
    text-align: center;
    font-size: 36px;
    font-weight: 800;
  }
  .contact-title {
    position: absolute;
    left: 0; right: 0;
    top: 192px;
    margin: 0;
    text-align: center;
    font-family: "EB Garamond", serif;
    font-size: 26px;
    color: var(--muted);
  }
  .divider {
    position: absolute;
    left: 214px;
    top: 279px;
  }
  .contact-line {
    position: absolute;
    left: 0; right: 0;
    margin: 0;
    text-align: center;
    font-size: 24px;
    font-weight: 400;
  }
  .contact-line--phone { top: 327px; }
  .contact-line--email { top: 365px; }
  .contact-line--address { top: 437px; }
</style>
</head>
<body>
<main class="canvas">
  <section class="card card--back">
    <p class="mission">
      <span class="keyword">We help</span> [target demographic] <span class="keyword">achieve</span><br>
      [desired emotional outcome] <span class="keyword">by</span> [our<br>
      unique approach] <span class="keyword">because</span> [our brand<br>
      beliefs]
    </p>
  </section>

  <section class="card card--front">
    <h1 class="wordmark">NORTHVALE</h1>
    <h2 class="contact-name">Daniel Harrow</h2>
    <p class="contact-title">Brand Consultant</p>

    <svg class="divider" width="432" height="32" viewBox="0 0 432 32" aria-hidden="true">
      <defs>
        <linearGradient id="rule-left" x1="0" x2="1">
          <stop offset="0" stop-color="#009ad8" stop-opacity="0"/>
          <stop offset="1" stop-color="#009ad8"/>
        </linearGradient>
        <linearGradient id="rule-right" x1="0" x2="1">
          <stop offset="0" stop-color="#009ad8"/>
          <stop offset="1" stop-color="#009ad8" stop-opacity="0"/>
        </linearGradient>
      </defs>
      <rect x="0" y="15" width="160" height="2" fill="url(#rule-left)"/>
      <rect x="272" y="15" width="160" height="2" fill="url(#rule-right)"/>
      <circle cx="190" cy="16" r="15.5" fill="#009ad8"/>
      <path d="M185 8.5c1-.6 2 .1 2.4 1l1.2 2.6c.3.8 0 1.5-.7 1.9l-1 .6c.5 2 1.8 3.9 3.4 5.2l1-.5c.8-.4 1.5-.2 2 .5l1.6 2.3c.5.8.3 1.8-.5 2.3-1.6 1-3.6 1-5.4-.4-3-2.4-5-6.1-5.4-9.7-.2-2 .3-4.3 1.4-5.8z" fill="#262626"/>
      <circle cx="241" cy="16" r="15.5" fill="#009ad8"/>
      <rect x="232" y="10" width="18" height="12" rx="1.5" fill="#262626"/>
      <path d="M233 11l8 6.5 8-6.5" stroke="#009ad8" stroke-width="1.4" fill="none"/>
      <path d="M233 21l6-5M249 21l-6-5" stroke="#009ad8" stroke-width="1.2" fill="none"/>
    </svg>

    <p class="contact-line contact-line--phone">5530 417 (555)</p>
    <p class="contact-line contact-line--email">daniel@northvale.com</p>
    <p class="contact-line contact-line--address">90417 Lakeview, CA 415 Harbor Ave, Ste 1180</p>
  </section>
</main>
</body>
</html>
```